I need a two page flyer (one page front and back) outlining our residential furniture rental options.

Title: Premium Residential Furniture Rentals

GOOD
Our Brimwell Orla Furniture Package is designed to offer a perfect balance of affordability and style, without compromising on quality. This package features a selection of functional and aesthetically pleasing furniture pieces, ideal for those looking to create a polished and professional space. With quick installation handled by our experienced in-house team, you can expect a smooth and hassle-free setup. This package ensures both convenience and value, providing a streamlined solution for your needs.
Living room, dining room and bedroom (additional bedrooms available)
- $710/month with a 3 month commitment
- $570/month with a 6 month commitment

BETTER
Our Premium Furniture Package takes comfort and style to the next level, offering an enhanced experience compared to our Orla option. Carefully selected with durability in mind, this package features high-quality, convenient furniture designed for both functionality and aesthetics. Perfect for those seeking a more refined look and superior comfort, it’s ideal for creating a sophisticated and inviting environment. With attention to detail in both design and craftsmanship, the premium package elevates any space, ensuring a higher standard of comfort and style that caters to both employees and clients.
- $1,150/month with a 3 month commitment
- $900/month with a 6 month commitment

BEST
Our Custom Furniture Package offers a tailored experience where you’ll work directly with our expert designer to create the ultimate luxurious and functional space. We include lounging, dining, sleeping and working from home, this package allows you to curate a space that perfectly fits your needs and style. With personalized attention to detail, we ensure every element is designed to provide the highest level of comfort, convenience, and elegance, transforming your space into a sophisticated sanctuary for relaxation and enjoyment.
Please inquire for pricing

www.quilbyhomeleasing.com

```html
<!DOCTYPE html>
<html lang="en">
<head>
<meta charset="utf-8">
<title>Premium Residential Furniture Rentals</title>
<link href="https://fonts.googleapis.com/css2?family=Montserrat:wght@300;400;500;700;800&display=swap" rel="stylesheet">
<style>
:root{
  --ink-navy:#313860;
  --card-body:#55577f;
  --band-light:#e6e4ef;
  --band-mid:#d1cde5;
  --copy:#6a6a80;
  --url:#555566;
  --phone:#4f4f55;
  --white:#ffffff;
}
*{margin:0;padding:0;box-sizing:border-box}
html,body{width:848px;height:1200px;overflow:hidden;background:var(--white)}
body{font-family:'Montserrat',sans-serif;position:relative}
.site-url{position:absolute;top:75px;left:0;width:848px;text-align:center;font-weight:400;font-size:15px;letter-spacing:5.2px;color:var(--url)}
.hero-photo{position:absolute;left:10px;top:146px;width:838px;height:287px;
  background:linear-gradient(90deg,#6b6562 0%,#4a4a4e 20%,#8d8d90 45%,#b9b9bb 65%,#7a726d 85%,#6a625d 100%)}
.tier{position:absolute;left:0;width:848px;height:211px}
.tier--good{top:433px;background:var(--band-light)}
.tier--better{top:644px;background:var(--band-mid)}
.tier--best{top:854px;height:210px;background:var(--band-light)}
.price-card{position:absolute;left:59px;top:25px;width:182px;height:160px;border-radius:24px;background:var(--card-body);overflow:hidden;color:var(--white);text-align:center}
.price-card__title{height:42px;background:var(--ink-navy);font-weight:800;font-size:25px;line-height:44px;letter-spacing:.5px}
.price{margin-top:6px}
.price + .price{margin-top:6px}
.price__amount{font-weight:300;font-size:31px;line-height:30px}
.price__unit{font-size:15px}
.price__term{font-weight:700;font-size:8.3px;letter-spacing:.1px;margin-top:1px}
.price-card__rule{width:40px;height:1px;background:var(--white);margin:7px auto 0}
.price-card__inquire{font-weight:400;font-size:18.5px;line-height:26px;padding-top:39px}
.tier__copy{position:absolute;left:276px;width:513px;font-size:12.2px;line-height:16.7px;color:var(--copy);text-align:justify;letter-spacing:.35px}
.tier--good .tier__copy{top:37px}
.tier--better .tier__copy{top:28px}
.tier--best .tier__copy{top:50px}
.brand{position:absolute;left:72px;top:1106px;display:flex;align-items:center;gap:12px}
.brand__mark{width:40px;height:40px;background:var(--ink-navy)}
.brand__text{color:var(--ink-navy)}
.brand__name{font-weight:400;font-size:17px;letter-spacing:.3px;line-height:20px}
.brand__services{font-weight:500;font-size:7.4px;letter-spacing:.9px;margin-top:6px}
.phone{position:absolute;left:527px;top:1109px;display:flex;align-items:center;gap:8px;font-weight:800;font-size:31px;color:var(--phone);letter-spacing:.3px}
</style>
</head>
<body>
<div class="site-url">www.quilbyhomeleasing.com</div>

<div class="hero-photo" role="img" aria-label="Bedroom furniture set with grey tufted headboard bed, striped bedding, nightstand with white lamp and grey wood dresser"></div>

<section class="tier tier--good">
  <div class="price-card">
    <div class="price-card__title">GOOD</div>
    <div class="price"><div class="price__amount">$710<span class="price__unit">/month</span></div><div class="price__term">with a 3 month commitment</div></div>
    <div class="price-card__rule"></div>
    <div class="price"><div class="price__amount">$570<span class="price__unit">/month</span></div><div class="price__term">with a 6 month commitment</div></div>
  </div>
  <p class="tier__copy">Our Brimwell Orla Furniture Package is designed to offer a perfect balance of affordability and style, without compromising on quality. This package features a selection of functional and aesthetically pleasing furniture pieces, ideal for those looking to create a polished and professional space. With quick installation handled by our experienced in-house team, you can expect a smooth and hassle-free setup. This package ensures both convenience and value, providing a streamlined solution for your needs. Living room, dining room and bedroom (additional bedrooms available)</p>
</section>

<section class="tier tier--better">
  <div class="price-card">
    <div class="price-card__title">BETTER</div>
    <div class="price"><div class="price__amount">$1,150<span class="price__unit">/month</span></div><div class="price__term">with a 3 month commitment</div></div>
    <div class="price-card__rule"></div>
    <div class="price"><div class="price__amount">$900<span class="price__unit">/month</span></div><div class="price__term">with a 6 month commitment</div></div>
  </div>
  <p class="tier__copy">Our Premium Furniture Package takes comfort and style to the next level, offering an enhanced experience compared to our Orla option. Carefully selected with durability in mind, this package features high-quality, convenient furniture designed for both functionality and aesthetics. Perfect for those seeking a more refined look and superior comfort, it’s ideal for creating a sophisticated and inviting environment. With attention to detail in both design and craftsmanship, the premium package elevates any space, ensuring a higher standard of comfort and style that caters to both employees and clients. Living room, dining room and bedroom (additional bedrooms available)</p>
</section>

<section class="tier tier--best">
  <div class="price-card">
    <div class="price-card__title">BEST</div>
    <div class="price-card__inquire">Please inquire<br>for pricing</div>
  </div>
  <p class="tier__copy">Our Custom Furniture Package offers a tailored experience where you’ll work directly with our expert designer to create the ultimate luxurious and functional space. We include lounging, dining, sleeping and working from home, this package allows you to curate a space that perfectly fits your needs and style. With personalized attention to detail, we ensure every element is designed to provide the highest level of comfort, convenience, and elegance, transforming your space into a sophisticated sanctuary for relaxation and enjoyment.</p>
</section>

<footer>
  <div class="brand">
    <div class="brand__mark"></div>
    <div class="brand__text">
      <div class="brand__name">QUILBY HOME LEASING</div>
      <div class="brand__services">STAGING | RESIDENTIAL | CORPORATE | SALES</div>
    </div>
  </div>
  <div class="phone">
    <svg width="18" height="28" viewBox="0 0 18 28" aria-hidden="true"><rect x="1.5" y="1.5" width="15" height="25" rx="3" fill="none" stroke="#313860" stroke-width="2.5"/><line x1="6" y1="4.5" x2="12" y2="4.5" stroke="#313860" stroke-width="2"/></svg>
    <span>555-240-7719</span>
  </div>
</footer>
</body>
</html>
```